New Modern High end Gin Design

We are looking for a new design for our current gin. The gin is named Oak Lantern Gin. We are looking for the bottle to be blue and the lettering to be gold. Please add the design on the bottle. the picture of the current bottle is in the uploaded files. we will not be using the same bottle. See photo attached with bottle type we would like to use. We would also like to make the rail cart imaged embossed

Font styles to use
Decorative

Colors
0054AA
0677BA
7BADD7
CADEEF
E8F1F8
0094D4
00A9DD
6FCCEA
C7EBF8
E9F6FB
FFC000
F8CF3A
FAE287
FDF2CF
FEFAEE

Requirements
Must have
• blue bottle
Nice to have
• ridges in the bottle

```html
<!DOCTYPE html>
<html lang="en">
<head>
<meta charset="utf-8">
<title>Oak Lantern Gin – Bottle Label</title>
<link rel="stylesheet" href="https://fonts.googleapis.com/css2?family=Arimo:wght@700&display=swap">
<style>
  :root {
    --page: #ffffff;
    --label-ground: #3d3d3f;
    --gold-text: #a8923a;
    --gold-line: #a08a35;
    --gold-light: #fae287;
    --gold-mid: #d9a53a;
    --gold-dark: #7a4a12;
    --batch-field: #c8c8c6;
    --glass-blue: #7badd7;
    --glass-deep: #0054aa;
  }
  html, body {
    margin: 0;
    padding: 0;
    width: 1200px;
    height: 1000px;
    overflow: hidden;
    background: var(--page);
  }
  .canvas {
    position: relative;
    width: 1200px;
    height: 1000px;
  }
  .label {
    position: absolute;
    left: 171px;
    top: 220px;
    width: 858px;
    height: 560px;
  }
  .label-ground { fill: var(--label-ground); }
  .frame-line {
    fill: none;
    stroke: var(--gold-line);
    stroke-width: 4;
    stroke-linecap: round;
  }
  .brand-name {
    font-family: "Arimo", Arial, sans-serif;
    font-weight: 700;
    font-size: 30px;
    fill: var(--gold-text);
    text-anchor: middle;
  }
  .spec {
    font-family: "Arimo", Arial, sans-serif;
    font-weight: 700;
    fill: var(--gold-text);
    text-anchor: middle;
  }
  .spec-large { font-size: 22px; }
  .spec-medium { font-size: 19px; }
  .spec-small { font-size: 15px; }
  .spec-tiny { font-size: 13px; }
  .batch-field { fill: var(--batch-field); }
</style>
</head>
<body>
<main class="canvas">
  <svg class="label" viewBox="0 0 858 560" xmlns="http://www.w3.org/2000/svg" aria-label="Oak Lantern Gin bottle label">
    <defs>
      <linearGradient id="gold-band" x1="0" x2="1" y1="0" y2="0">
        <stop offset="0" stop-color="var(--gold-mid)"/>
        <stop offset="0.25" stop-color="var(--gold-light)"/>
        <stop offset="0.5" stop-color="var(--gold-mid)"/>
        <stop offset="0.75" stop-color="var(--gold-dark)"/>
        <stop offset="1" stop-color="var(--gold-mid)"/>
      </linearGradient>
      <linearGradient id="gold-star" x1="0" x2="1" y1="0" y2="1">
        <stop offset="0" stop-color="var(--gold-light)"/>
        <stop offset="1" stop-color="var(--gold-dark)"/>
      </linearGradient>
      <radialGradient id="glass-glow" cx="0.5" cy="0.5" r="0.5">
        <stop offset="0" stop-color="var(--glass-deep)" stop-opacity="0.55"/>
        <stop offset="0.55" stop-color="var(--glass-blue)" stop-opacity="0.45"/>
        <stop offset="1" stop-color="#ffffff" stop-opacity="0"/>
      </radialGradient>
      <polygon id="star" points="0,-19 5.6,-6 19,-5.9 8.8,3.4 11.8,17 0,9.6 -11.8,17 -8.8,3.4 -19,-5.9 -5.6,-6"/>
    </defs>

    <rect class="label-ground" x="0" y="0" width="858" height="560"/>

    <rect class="gold-band top" x="0" y="20" width="858" height="11" fill="url(#gold-band)"/>
    <rect class="gold-band bottom" x="0" y="528" width="858" height="11" fill="url(#gold-band)"/>

    <g class="rating-stars" fill="url(#gold-star)">
      <use href="#star" x="123" y="187"/>
      <use href="#star" x="123" y="273"/>
      <use href="#star" x="123" y="367"/>
    </g>

    <path class="frame-line" d="M238 62 V480 Q238 495 253 495 H610 Q625 495 625 480 V200"/>

    <rect class="bottle-illustration" x="310" y="95" width="240" height="345" rx="60"
          fill="url(#glass-glow)" role="img"
          aria-label="Illustration of a tilted clear glass gin bottle with a blue cap and soft glow"/>

    <text class="brand-name" x="431" y="480">Oak Lantern Gin</text>

    <g class="specs">
      <text class="spec spec-large" x="748" y="160">VOL.</text>
      <text class="spec spec-large" x="748" y="187">750ML</text>
      <text class="spec spec-large" x="748" y="249">ROOOF.</text>
      <text class="spec spec-large" x="748" y="274">80</text>
      <text class="spec spec-medium" x="748" y="318">BATCH #.</text>
      <rect class="batch-field" x="695" y="331" width="95" height="38"/>
      <text class="spec spec-small" x="748" y="401">BRAMBLE FORD,NJ</text>
      <text class="spec spec-tiny" x="748" y="419">ALC by VOL. 40%</text>
    </g>
  </svg>
</main>
</body>
</html>
```